Modern business card design for professional copywriter

I'd like a business card design that I can use to have my cards printed out by plink.com as a squared corners business card (see artwork and design guidelines here: https://help.plink.com/hc/en-gb/sections/300481726-PLINK-Product-Templates)

The design should be clean and modern and reflect the colours, tone and branding on my website: https://noravestrel.com.au

Target Market(s)

Professionals, B2B small business owners

Industry/Entity Type

Business

Contact Information for Business Card

Nora Vestrel
m: 0427 593 864
e: nora@noravestrel.com.au
w: noravestrel.com.au

Font styles to use
Sans Serif

Requirements
Must have
• Tagline: "Smart copywriting for clever business people"
• Brand colours: fd8000, 009984, 666666 and black
Nice to have

```html
<!DOCTYPE html>
<html lang="en">
<head>
<meta charset="utf-8">
<title>Nora Vestrel – Business Card</title>
<link rel="stylesheet" href="https://fonts.googleapis.com/css2?family=Mulish:wght@400;700&display=swap">
<style>
  :root {
    --backdrop: #e5e5e5;
    --card-dark: #050505;
    --card-light: #fbf8f4;
    --brand-orange: #fd8000;
    --brand-teal: #009984;
    --brand-grey: #666666;
    --text-grey: #5a5a5a;
  }
  * { margin: 0; padding: 0; box-sizing: border-box; }
  html, body {
    width: 1200px;
    height: 1000px;
    overflow: hidden;
    background: var(--backdrop);
    font-family: "Mulish", "Century Gothic", sans-serif;
  }
  .canvas {
    position: relative;
    width: 1200px;
    height: 1000px;
  }
  .card {
    position: absolute;
    top: 330px;
    width: 340px;
    height: 340px;
  }
  .card--front {
    left: 230px;
    background: var(--card-dark);
  }
  .card--back {
    left: 630px;
    background: var(--card-light);
  }

  /* Front: name lockup */
  .front-lockup {
    position: absolute;
    left: 50%;
    top: 50%;
    transform: translate(-50%, -50%);
    text-align: right;
  }
  .front-name {
    display: flex;
    align-items: center;
    gap: 10px;
    font-size: 34px;
    font-weight: 700;
    color: var(--brand-teal);
    white-space: nowrap;
  }
  .front-name__mark {
    width: 14px;
    height: 14px;
    background: var(--brand-orange);
  }
  .front-role {
    margin-top: 2px;
    font-size: 11px;
    letter-spacing: 5px;
    color: var(--brand-grey);
  }

  /* Back: name, tagline and contact details */
  .back-heading {
    position: absolute;
    left: 34px;
    top: 96px;
    right: 34px;
  }
  .back-name {
    font-size: 20px;
    font-weight: 700;
    color: var(--brand-teal);
  }
  .back-name__surname { color: var(--brand-grey); }
  .tagline {
    margin-top: 6px;
    font-size: 11px;
    line-height: 15px;
    color: var(--brand-grey);
  }
  .contact-list {
    position: absolute;
    left: 34px;
    bottom: 40px;
    list-style: none;
  }
  .contact-item {
    display: flex;
    align-items: center;
    gap: 8px;
    font-size: 15px;
    line-height: 22px;
    color: var(--text-grey);
  }
  .contact-item svg {
    width: 13px;
    height: 13px;
    flex: none;
  }
</style>
</head>
<body>
<main class="canvas">
  <section class="card card--front" aria-label="Business card front">
    <div class="front-lockup">
      <div class="front-name"><span class="front-name__mark"></span>Nora Vestrel</div>
      <div class="front-role">COPYWRITER</div>
    </div>
  </section>

  <section class="card card--back" aria-label="Business card back">
    <div class="back-heading">
      <h1 class="back-name">Nora <span class="back-name__surname">Vestrel</span></h1>
      <p class="tagline">Smart copywriting for clever business people</p>
    </div>
    <ul class="contact-list">
      <li class="contact-item">
        <svg viewBox="0 0 14 14" aria-hidden="true"><rect x="3.5" y="1" width="7" height="12" rx="1" fill="none" stroke="var(--brand-orange)" stroke-width="1.4"/><circle cx="7" cy="11" r="0.8" fill="var(--brand-orange)"/></svg>
        <span>0427 593 864</span>
      </li>
      <li class="contact-item">
        <svg viewBox="0 0 14 14" aria-hidden="true"><rect x="1" y="3" width="12" height="8" fill="var(--brand-orange)"/><path d="M1 3 L7 8 L13 3" fill="none" stroke="var(--card-light)" stroke-width="1"/></svg>
        <span>nora@noravestrel.com.au</span>
      </li>
      <li class="contact-item">
        <svg viewBox="0 0 14 14" aria-hidden="true"><circle cx="7" cy="7" r="6" fill="var(--brand-orange)"/><path d="M1 7 H13 M7 1 C4 4 4 10 7 13 M7 1 C10 4 10 10 7 13" fill="none" stroke="var(--card-light)" stroke-width="0.9"/></svg>
        <span>noravestrel.com.au</span>
      </li>
    </ul>
  </section>
</main>
</body>
</html>
```